Business Card Re-Design

Consulting Company: To build a high performance organization, you need great leaders at all levels throughout your organization. The Northvale Talent Growth Studio engages, inspires, and educates current and future leaders to step beyond the ordinary and deliver exceptional results. This new breed of leaders will motivate your staff to leave the safety of complacency behind and come together to build an extraordinary organization. The current trend has been to ask our people to do more with fewer resources. People have been stepping up to the challenge, but more is required to ensure success with a new work paradigm. We work with your management team to build a successful strategy that will make your organization more effective. NTGS then supports your management team by providing a comprehensive set of proven services to empower your entire organization to successfully execute new strategies.Let NTGS help you optimize your organization’s individual and team performance today!

Target Market(s)

Federal, State and Local Government / Non profit

Industry/Entity Type

Management Consulting

Contact Information for Business Card

NTGS, inc (Northvale Talent Growth Studio) Optimizing Individual and Organizational Performance

Colors
fee18a
ec1f27
474747
fbf289

Requirements
Must have
• Professional and high quality feel

```html
<!DOCTYPE html>
<html lang="en">
<head>
<meta charset="utf-8">
<title>NTGS Business Card</title>
<link href="https://fonts.googleapis.com/css2?family=Open+Sans:wght@400;600;700&display=swap" rel="stylesheet">
<style>
  :root {
    --page: #ecebe9;
    --card-white: #ffffff;
    --band-grey: #878787;
    --mark-grey: #9a9a9a;
    --text-light: #ffffff;
    --rule: rgba(255,255,255,0.22);
  }
  * { box-sizing: border-box; margin: 0; padding: 0; }
  html, body { width: 1200px; height: 900px; overflow: hidden; }
  body {
    background: var(--page);
    position: relative;
    font-family: "Open Sans", Arial, sans-serif;
  }
  .card {
    position: absolute;
    background: var(--card-white);
    box-shadow: 0 4px 14px rgba(0,0,0,0.12);
    overflow: hidden;
  }
  /* Front */
  .card--front { left: 77px; top: 34px; width: 589px; height: 364px; }
  .front__brand {
    position: absolute; left: 32px; top: 54px;
    display: flex; align-items: center; gap: 10px;
  }
  .brand__square { width: 14px; height: 14px; background: var(--mark-grey); }
  .brand__name {
    font-size: 46px; font-weight: 700; color: var(--mark-grey);
    letter-spacing: 1px; line-height: 1;
  }
  .front__band {
    position: absolute; left: 0; top: 156px; width: 100%; height: 208px;
    background: var(--band-grey); color: var(--text-light);
  }
  .person__name {
    position: absolute; left: 30px; top: 20px;
    font-size: 19px; font-weight: 600; letter-spacing: 0.3px;
  }
  .detail-rule {
    position: absolute; left: 0; width: 248px; height: 1px; background: var(--rule);
  }
  .person__title { position: absolute; left: 36px; top: 62px; font-size: 15px; }
  .contact {
    position: absolute; left: 32px; display: flex; align-items: center; gap: 7px;
    font-size: 15px;
  }
  .contact svg { width: 11px; height: 11px; fill: var(--text-light); }
  .address { position: absolute; left: 30px; top: 169px; font-size: 15px; }
  /* Back */
  .card--back { left: 388px; top: 505px; width: 567px; height: 352px; }
  .back__band {
    position: absolute; left: 0; top: 90px; width: 100%; height: 172px;
    background: var(--band-grey);
    display: flex; align-items: center; justify-content: center; gap: 12px;
  }
  .back__band .brand__square { background: var(--text-light); width: 16px; height: 16px; }
  .back__band .brand__name { color: var(--text-light); font-size: 56px; }
</style>
</head>
<body>
  <section class="card card--front">
    <div class="front__brand">
      <span class="brand__square"></span>
      <span class="brand__name">NTGS</span>
    </div>
    <div class="front__band">
      <p class="person__name">DANIEL R.MERCER</p>
      <span class="detail-rule" style="top:55px"></span>
      <p class="person__title">President/CEO</p>
      <span class="detail-rule" style="top:87px"></span>
      <p class="contact" style="top:94px">
        <svg viewBox="0 0 12 12"><path d="M2.5 0.5 4.5 3 3.5 4.5c.7 1.6 2 2.9 3.6 3.6L8.6 7 11.5 9 10.5 11.2C5 11 1 7 0.8 1.5z"/></svg>
        410.555.0182</p>
      <span class="detail-rule" style="top:115px"></span>
      <p class="contact" style="top:116px">
        <svg viewBox="0 0 12 12"><path d="M3 0h5v3H3zM1 4h10v7H1zM3 6v1h2V6zm4 0v1h2V6zM3 8v1h2V8zm4 0v1h2V8z"/></svg>
        410.555.0147</p>
      <span class="detail-rule" style="top:137px"></span>
      <p class="contact" style="top:138px">
        <svg viewBox="0 0 12 12"><path d="M0 2h12v1L6 7 0 3zM0 4.2l6 4 6-4V10H0z"/></svg>
        contact@northvalestudio.com</p>
      <span class="detail-rule" style="top:161px"></span>
      <p class="address">2450 Linden Ridge Road Northvale, MD 20900</p>
    </div>
  </section>

  <section class="card card--back">
    <div class="back__band">
      <span class="brand__square"></span>
      <span class="brand__name">NTGS</span>
    </div>
  </section>
</body>
</html>
```